Wine Bottle Label

Project: New Label for Marlow Wine

Sponsored by: Tall Oak Cellars (talloakcellars.example and Castellane Wines, producer of Marlow Wines)

Product Description:

Wine comes in both red (cabernet, zinfandel) and white (Chardonnay, Sauvignon Blanc). It is marketed to restaurants and mid priced retailers including Harbor Pantry, etc.) Wine is priced between $17 - $20 per bottle. The wine is in the medium price category and is intended for mid market appeal.

_
Label Requirements:

• Noticeable among other labels when on a black bottle. White labels are most noticeable but all color choices are an option if the brand stands out and can be easily recognizable from 10 – 12ft.

• Has to appeal to Gen X - younger people. Contemporary. Must appeal to women who buy the majority of wine in the US.

• Has to be presentable at the dinner table...slightly sophisticated.

• Has to connect with the “Official Bird of the Fenwick Nature League” Great White Marlow

• Bird is most often seen in grassy green pasture/meadows or wading in shallow water. Alone or in group.

• Has to fit on the bottle: Label size: 3 ½” H – 2 ¾” W

• Keep it Simple, lots of empty space

• Could be free form graphic design, illustrations, photos, etc.

• Could be abstract representation providing it connects to Egrets, e.g. stamp of foot which is gold embossed or similar.)

• Label must contain:

o Brand Name: Marlow
o Varietal: will vary (Cabernet Sauvignon, Chardonnay, Sauvignon Blanc, Zinfandel, etc.)
o Appellation: varies (Sonoma County, Napa Valley, California)
o Vintage: 2010, 2011, etc.

• Variations in label color/design are possible between varietals but brand should be consistent.

Back design must also be included. Example of current back with text is attached.

Requirements
Must have
• Must have relationship with Marlow Bird - figuratively or literally
Has to fit on the bottle: Label size: 3 ½” H – 2 ¾” W
o Brand Name: Marlow

```html
<!DOCTYPE html>
<html lang="en">
<head>
<meta charset="utf-8">
<title>Marlow Wine – Label Range</title>
<link rel="stylesheet" href="https://fonts.googleapis.com/css2?family=Antonio:wght@100;300;400&display=swap">
<style>
  :root {
    --backdrop: #1d1b1d;
    --label-white: #ffffff;
    --cabernet: #8a5bb5;
    --chardonnay: #8cc63f;
    --zinfandel: #d4145a;
    --sauvignon-blanc: #3dba6a;
  }
  * { margin: 0; padding: 0; box-sizing: border-box; }
  html, body {
    width: 1200px;
    height: 671px;
    overflow: hidden;
    background: var(--backdrop);
  }
  .label-range {
    position: relative;
    width: 1200px;
    height: 671px;
  }
  .label {
    position: absolute;
    top: 185px;
    width: 230px;
    height: 291px;
    background: var(--label-white);
    display: flex;
    flex-direction: column;
    align-items: center;
    font-family: "Antonio", "Arial Narrow", sans-serif;
    color: var(--tone);
  }
  .label--cabernet { left: 36px; --tone: var(--cabernet); }
  .label--chardonnay { left: 331px; --tone: var(--chardonnay); }
  .label--zinfandel { left: 631px; --tone: var(--zinfandel); }
  .label--sauvignon-blanc { left: 935px; --tone: var(--sauvignon-blanc); }

  .label__emblem {
    margin-top: 51px;
    width: 88px;
    height: 88px;
  }
  .label__brand {
    margin-top: 40px;
    font-weight: 100;
    font-size: 38px;
    line-height: 36px;
    letter-spacing: 2px;
    padding-left: 2px;
  }
  .label__varietal {
    margin-top: 2px;
    background: var(--tone);
    color: var(--label-white);
    font-weight: 300;
    font-size: 21px;
    line-height: 23px;
    letter-spacing: 0.5px;
    text-transform: uppercase;
    padding: 0 4px;
    text-align: left;
  }
  .label__details {
    margin-top: 2px;
    font-weight: 300;
    font-size: 13px;
    line-height: 15px;
    letter-spacing: 1.5px;
    padding-left: 1.5px;
  }
</style>
</head>
<body>
<main class="label-range">

  <section class="label label--cabernet">
    <svg class="label__emblem" viewBox="0 0 88 88" aria-hidden="true">
      <circle cx="44" cy="44" r="44" fill="var(--cabernet)" opacity="0.25"/>
    </svg>
    <h2 class="label__brand">MARLOW</h2>
    <p class="label__varietal">Cabernet<br>Sauvignon</p>
    <p class="label__details">2013 \ CALIFORNIA</p>
  </section>

  <section class="label label--chardonnay">
    <svg class="label__emblem" viewBox="0 0 88 88" aria-hidden="true">
      <circle cx="44" cy="44" r="44" fill="var(--chardonnay)" opacity="0.35"/>
    </svg>
    <h2 class="label__brand">MARLOW</h2>
    <p class="label__varietal">Chardonnay</p>
    <p class="label__details">2013 \ CALIFORNIA</p>
  </section>

  <section class="label label--zinfandel">
    <svg class="label__emblem" viewBox="0 0 88 88" aria-hidden="true">
      <circle cx="44" cy="44" r="44" fill="var(--zinfandel)" opacity="0.22"/>
    </svg>
    <h2 class="label__brand">MARLOW</h2>
    <p class="label__varietal">Zinfandel</p>
    <p class="label__details">2013 \ CALIFORNIA</p>
  </section>

  <section class="label label--sauvignon-blanc">
    <svg class="label__emblem" viewBox="0 0 88 88" aria-hidden="true">
      <circle cx="44" cy="44" r="44" fill="var(--sauvignon-blanc)" opacity="0.3"/>
    </svg>
    <h2 class="label__brand">MARLOW</h2>
    <p class="label__varietal">Sauvignon<br>Blanc</p>
    <p class="label__details">2013 \ CALIFORNIA</p>
  </section>

</main>
</body>
</html>
```